BHG Letterhead

I need letterhead for "birch hollow gateway llc" ...

logo attached to project..

Company Info:
482 South Marigold Avenue, Suite 7D
Chicago, Illinois 60617
ofc 312-555-0148
facsimile 312-555-0193
www.birchhollowgatewayllc.example
info@birchhollowgatewayllc.example

I have multiple projects listed.. see below:

Business cards for birch hollow gateway llc
letterhead "
envelopes "

Business cards for KP Vending LLC
letterhead "
envelopes "

Industry/Entity Type

It Company

```html
<!DOCTYPE html>
<html lang="en">
<head>
<meta charset="utf-8">
<title>Birch Hollow Gateway LLC Letterhead</title>
<link rel="stylesheet" href="https://fonts.googleapis.com/css2?family=Cinzel:wght@400&family=Crimson+Text:wght@400&display=swap">
<style>
  :root {
    --brand-blue: #1f4e8c;
    --ink-gray: #4a4a4a;
    --paper: #ffffff;
    --edge: #bdbdbd;
    --watermark: #f1f1f1;
  }
  * { margin: 0; padding: 0; box-sizing: border-box; }
  html, body { width: 928px; height: 1200px; overflow: hidden; background: var(--paper); }
  .letterhead {
    position: relative;
    width: 928px;
    height: 1200px;
    background: var(--paper);
    border: 1px solid var(--edge);
    overflow: hidden;
  }
  .brand-watermark {
    position: absolute;
    left: 0;
    top: 0;
    width: 928px;
    height: 1200px;
  }
  .brand-mark {
    position: absolute;
    left: 112px;
    top: 34px;
    width: 70px;
    height: 70px;
    border-radius: 50%;
    background: var(--brand-blue);
  }
  .company-header {
    position: absolute;
    left: 27px;
    top: 112px;
  }
  .company-name {
    font-family: "Cinzel", serif;
    font-weight: 400;
    font-size: 19px;
    line-height: 22px;
    color: var(--brand-blue);
    letter-spacing: 0.2px;
    white-space: nowrap;
  }
  .company-name .suffix { font-size: 11px; letter-spacing: 0.6px; }
  .contact-list {
    list-style: none;
    margin-top: -2px;
    font-family: "Crimson Text", serif;
    font-size: 14px;
    line-height: 15.2px;
    font-variant-numeric: oldstyle-nums;
    color: var(--ink-gray);
  }
  .contact-list .web { color: var(--brand-blue); }
</style>
</head>
<body>
  <main class="letterhead">
    <svg class="brand-watermark" viewBox="0 0 928 1200" role="img" aria-label="Large faint brand symbol watermark across the lower right of the page">
      <circle cx="585" cy="790" r="500" fill="var(--watermark)"/>
    </svg>
    <div class="brand-mark" aria-hidden="true"></div>
    <header class="company-header">
      <h1 class="company-name">Birch Hollow Gateway <span class="suffix">LLC</span></h1>
      <ul class="contact-list">
        <li>482 South Marigold Avenue, Suite 7D</li>
        <li>Chicago, Illinois 60617</li>
        <li>Office: 312-555-0148</li>
        <li>Facsimile: 312-555-0193</li>
        <li class="web">www.birchhollowgatewayllc.example</li>
        <li>info@birchhollowgatewayllc.example</li>
      </ul>
    </header>
  </main>
</body>
</html>
```